Motivationskarten für Trainer und Coach
Zielgruppe
Ich bin Trainer und Coach mit Schwerpunkt Effizienz/ Zeit- und Selbstmanagement sowie Büroorganisation. Meine Kunden buchen bei mir Seminare, um Ihren Arbeitsalltag effizienter zu gestalten und zu strukturieren und Ihre Büroabläufe sowie Prozesse zu optimieren.
Ich möchte gerne 3 verschiedene Postkarten mit Sprüchen von mir gestalten. Postkarten, die man auch verschicken kann und aus denen natürlich meine Kontaktdaten hervorgehen. Mein Logo sollte irgendwo auf der beschreibbaren Seite sichtbar sein. Vorne drauf nur der Spruch und vielleicht eine Zeichnung, eine Karikatur, eine Comiczeichnung oder ein Bild (ich bin offen für alles).
Die Sprüche lauten:
Lieber unperfekt anfangen als gar nicht!
Mach Dir hin und wieder bewusst, wie großartig Du bist!
Frage Dich immer: 'Was ist das Schlimmste, was passieren könnte?' - Es ist selten ein Weltuntergang.
Es sollen drei verschiedene Karten sein, die aber irgendwie zusammenpassen vom Design her.
Meine Hauptzielgruppe, für die auch diese Postkarten hier gedacht sind, sind vor allem Frauen - entweder Frauen, die als Assistentin arbeiten oder selbständig sind.
Aufgabenstellung
Es darf gerne etwas weiblich sein, sollte aber nicht zu bunt und schnörkelig sein. Es darf gerne auffallen. Achtung: Mein Logo sollte ohne Untertitel verwendet werden. Also nur 'Wiebke Harlach' - ohne 'Training & Coaching'.

```html
<!DOCTYPE html>
<html lang="de">
<head>
<meta charset="utf-8">
<title>Motivationskarte – Weltuntergang</title>
<link rel="stylesheet" href="https://fonts.googleapis.com/css2?family=Lobster+Two:wght@700&family=Amatic+SC:wght@400&display=swap">
<style>
  :root {
    --paper: #ffffff;
    --frame: #6d6fb2;
    --panel: #eaeaf5;
    --ink: #111111;
    --meadow-light: #e6ec5a;
    --meadow-mid: #a9cc3c;
    --meadow-sky: #d9ece6;
    --skin: #e8b193;
  }
  * { margin: 0; padding: 0; box-sizing: border-box; }
  html, body { width: 1200px; height: 851px; overflow: hidden; background: var(--paper); }
  .card {
    position: relative;
    width: 1200px;
    height: 851px;
    background: var(--paper);
  }
  .card__photo {
    position: absolute;
    left: 40px; top: 47px;
    width: 1120px; height: 756px;
    background:
      radial-gradient(ellipse 55% 60% at 30% 75%, var(--skin) 0%, rgba(232,177,147,0.85) 45%, rgba(232,177,147,0) 75%),
      radial-gradient(ellipse 40% 30% at 40% 5%, var(--meadow-light) 0%, rgba(230,236,90,0) 70%),
      linear-gradient(100deg, var(--meadow-mid) 0%, #c4d84a 35%, var(--meadow-sky) 70%, #b8d66a 100%);
  }
  .card__frame {
    position: absolute;
    left: 540px; top: 105px;
    width: 585px; height: 625px;
  }
  .quote {
    position: absolute;
    color: var(--ink);
    font-family: "Lobster Two", cursive;
    font-weight: 700;
    white-space: nowrap;
    line-height: 1;
  }
  .quote--line1 { left: 689px; top: 212px; font-size: 56px; }
  .quote--accent {
    left: 622px; top: 262px;
    font-family: "Amatic SC", cursive;
    font-weight: 400;
    font-size: 88px;
    transform: rotate(12deg);
    transform-origin: left top;
    letter-spacing: -1px;
  }
  .quote--was { left: 880px; top: 318px; font-size: 56px; }
  .quote--line3 { left: 598px; top: 388px; font-size: 56px; }
  .quote--line4 { left: 614px; top: 518px; font-size: 56px; }
  .quote--line5 { left: 641px; top: 590px; font-size: 56px; }
</style>
</head>
<body>
  <main class="card">
    <div class="card__photo" role="img" aria-label="Foto: vier Finger mit aufgemalten fröhlichen Gesichtern vor grüner Frühlingswiese"></div>

    <svg class="card__frame" viewBox="540 105 585 625" width="585" height="625" aria-hidden="true">
      <path fill="var(--frame)"
        d="M590 115 L1075 115 A35 35 0 0 0 1110 150 L1110 683 A35 35 0 0 0 1075 718 L590 718 A35 35 0 0 0 555 683 L555 150 A35 35 0 0 0 590 115 Z"/>
      <path fill="var(--panel)" fill-opacity="0.94"
        d="M600 131 L1065 131 A29 29 0 0 0 1094 160 L1094 673 A29 29 0 0 0 1065 702 L600 702 A29 29 0 0 0 571 673 L571 160 A29 29 0 0 0 600 131 Z"/>
      <path fill="none" stroke="var(--frame)" stroke-width="1.5" stroke-dasharray="2 2"
        d="M602 135 L1063 135 A27 27 0 0 0 1090 162 L1090 671 A27 27 0 0 0 1063 698 L602 698 A27 27 0 0 0 575 671 L575 162 A27 27 0 0 0 602 135 Z"/>
      <g fill="var(--ink)" font-family="Arial, sans-serif" font-weight="700" font-size="34" text-anchor="middle">
        <text x="562" y="140">*</text>
        <text x="1100" y="140">*</text>
        <text x="565" y="718">*</text>
        <text x="1104" y="716">*</text>
      </g>
    </svg>

    <p class="quote quote--line1">Was ist das</p>
    <p class="quote quote--accent">SCHLIMMSTE,</p>
    <p class="quote quote--was">was</p>
    <p class="quote quote--line3">passieren könnte?</p>
    <p class="quote quote--line4">– Es ist selten ein</p>
    <p class="quote quote--line5">Weltuntergang</p>
  </main>
</body>
</html>
```